Webpage

I am a professional genealogist. I need a webpage that is professional looking (using the logo I chose), I can add hyperlinks and photos to if and when I want.

```html
<!DOCTYPE html>
<html lang="en">
<head>
<meta charset="utf-8">
<title>Lineage Research – Professional Genealogist</title>
<link href="https://fonts.googleapis.com/css2?family=Open+Sans:wght@300;400;600;700&display=swap" rel="stylesheet">
<style>
:root{
  --teal:#1ea5b9;
  --teal-dark:#15889a;
  --teal-light:#35b9cc;
  --ink:#444;
  --muted:#8a8a8a;
  --line:#dcdcdc;
  --paper:#ffffff;
  --page:#f3f4f4;
  --green:#86b83e;
  --green-dark:#6d9a2c;
  --foot:#3b3c3d;
  --foot-deep:#2b2c2d;
  --foot-text:#c9c9c9;
}
*{box-sizing:border-box;margin:0;padding:0}
html,body{width:742px;height:1200px;overflow:hidden}
body{font-family:"Open Sans",Arial,sans-serif;color:var(--ink);background:var(--page);font-size:10px;line-height:1.5}
.page{width:742px;height:1200px;position:relative;background:var(--page)}

/* header */
.site-header{height:88px;background:var(--paper);display:flex;align-items:center;justify-content:space-between;padding:0 49px}
.brand{display:flex;align-items:center;gap:10px}
.brand-dot{width:38px;height:38px;border-radius:50%;background:var(--teal)}
.brand-name{font-size:17px;font-weight:600;color:var(--teal-dark)}
.call{text-align:right}
.call-label{font-size:11px;color:var(--muted)}
.call-number{font-size:18px;color:var(--teal);font-weight:400;letter-spacing:.3px}

/* nav */
.main-nav{height:36px;background:linear-gradient(var(--teal-light),var(--teal));padding:0 49px;display:flex}
.main-nav a{color:#fff;text-decoration:none;font-size:10.5px;font-weight:600;line-height:36px;padding:0 24px}
.main-nav a.active{background:var(--teal-dark)}

/* hero */
.hero{height:270px;position:relative;background:linear-gradient(100deg,#e9eef1 0%,#d4e3ea 35%,#c7dfe8 55%,#e6eef2 100%)}
.hero-photo{position:absolute;inset:0}
.hero-caption{position:absolute;left:452px;top:150px;width:230px}
.hero-caption h2{font-size:20px;font-weight:400;color:#333;margin-bottom:6px}
.hero-caption p{font-size:9.5px;color:#555}

/* main */
.content{height:569px;background:var(--paper);margin:0 49px;padding:20px 0 0}
.section-title{font-size:21px;font-weight:400;color:var(--teal);margin-bottom:10px}
.tabs{display:flex;border-bottom:1px solid var(--line)}
.tab{font-size:9.5px;color:#555;padding:5px 12px;border:1px solid var(--line);border-bottom:none;background:#f5f5f5;margin-right:-1px}
.tab.active{background:var(--paper);color:var(--ink);position:relative;top:1px}
.service-panel{border:1px solid var(--line);border-top:none;height:240px;display:flex;padding:22px 18px;gap:18px}
.service-photo{width:143px;height:150px;background:linear-gradient(135deg,#bcd9e2,#e9f0f2 60%,#9ec4cf);flex:none}
.service-body h3{font-size:19px;font-weight:400;color:var(--teal);margin-bottom:8px;padding-bottom:6px;border-bottom:1px solid var(--line)}
.service-body p{font-size:9.5px;color:#666;line-height:1.65;margin-bottom:12px}
.btn{display:inline-block;background:var(--green);color:#fff;font-size:9.5px;font-weight:600;padding:6px 14px;border-radius:3px;border-bottom:2px solid var(--green-dark);text-decoration:none}

.lower{display:flex;gap:20px;margin-top:30px}
.welcome{width:422px}
.sub-title{font-size:17px;font-weight:400;color:var(--teal);padding-bottom:6px;border-bottom:1px solid var(--line);margin-bottom:12px}
.welcome-row{display:flex;gap:12px}
.welcome-photo{width:140px;height:124px;background:linear-gradient(135deg,#d8e6ea,#f4f7f8 55%,#b9ccd2);flex:none}
.welcome-row p{font-size:9.5px;color:#666;line-height:1.7}
.news{flex:1}
.news-head{display:flex;justify-content:space-between;align-items:baseline;border-bottom:1px solid var(--line);padding-bottom:6px;margin-bottom:12px}
.news-head h3{font-size:17px;font-weight:400;color:var(--teal)}
.arrows{color:#aaa;font-size:14px;letter-spacing:6px}
.news-item{display:flex;gap:10px;margin-bottom:14px}
.news-thumb{width:42px;height:42px;border-radius:50%;background:linear-gradient(135deg,#cfe0e6,#9fc0ca);flex:none}
.news-item h4{font-size:9.5px;font-weight:400;color:var(--teal)}
.news-item p{font-size:9px;color:#777;line-height:1.5}

/* footer */
.site-footer{height:197px;background:var(--foot);padding:22px 49px 0;display:flex;color:var(--foot-text)}
.foot-col h4{font-size:13px;font-weight:400;color:#eee;margin-bottom:12px}
.foot-map{width:236px}
.map-area{width:150px;height:96px;background:linear-gradient(135deg,#e4e8e2,#cfd9d0 50%,#dfe4ea)}
.foot-contact{width:250px;font-size:9.5px}
.contact-line{display:flex;gap:8px;margin-bottom:10px;line-height:1.5}
.contact-line svg{flex:none;margin-top:2px}
.foot-follow{flex:1;font-size:9.5px}
.social{display:flex;gap:7px;margin-top:12px}
.social span{width:20px;height:20px;border-radius:50%;background:#6a6b6c}
.bottom-bar{height:40px;background:var(--foot-deep);color:#999;font-size:9px;line-height:40px;padding:0 49px}
</style>
</head>
<body>
<div class="page">
  <header class="site-header">
    <div class="brand">
      <span class="brand-dot"></span>
      <span class="brand-name">Lineage Research</span>
    </div>
    <div class="call">
      <div class="call-label">Call Dana today</div>
      <div class="call-number">+61 2 5550 1234</div>
    </div>
  </header>

  <nav class="main-nav">
    <a class="active" href="#">HOME</a>
    <a href="#">ABOUT US</a>
    <a href="#">SERVICES</a>
    <a href="#">CONTACT US</a>
    <a href="#">PUBLICATIONS</a>
    <a href="#">BLOG</a>
    <a href="#">LINKS</a>
  </nav>

  <section class="hero">
    <div class="hero-photo" role="img" aria-label="Researcher in cap and mask working in a bright laboratory"></div>
    <div class="hero-caption">
      <h2>Forensic genealogy</h2>
      <p>Trace every branch of your family with careful, documented research built on records, archives and decades of practice.</p>
    </div>
  </section>

  <main class="content">
    <h2 class="section-title">Our Services</h2>
    <div class="tabs">
      <span class="tab active">Forensic genealogy</span>
      <span class="tab">kinship determination</span>
      <span class="tab">Research analysis &amp; consultation</span>
      <span class="tab">Texas researcher</span>
      <span class="tab">Record retrieval</span>
    </div>
    <div class="service-panel">
      <div class="service-photo" role="img" aria-label="Scientists examining samples under a microscope"></div>
      <div class="service-body">
        <h3>Forensic genealogy</h3>
        <p>We work with courts, lawyers and estate executors to locate missing heirs and establish kinship. Each case combines civil registers, probate files, census returns and newspapers into a clear report. Findings are sourced, verified and presented so they stand up to scrutiny and answer the questions that matter.</p>
        <a class="btn" href="#">READ MORE</a>
      </div>
    </div>

    <div class="lower">
      <section class="welcome">
        <h3 class="sub-title">Welcome to Lineage Research Services</h3>
        <div class="welcome-row">
          <div class="welcome-photo" role="img" aria-label="Stethoscope resting on a desk"></div>
          <p>Every family has a story waiting in the records. I help clients uncover ancestors, confirm relationships and preserve what they find for the next generation. Whether you are starting out or stuck on a hard case, research is tailored to your goals and budget.</p>
        </div>
      </section>
      <aside class="news">
        <div class="news-head">
          <h3>Latest News</h3>
          <span class="arrows">‹ ›</span>
        </div>
        <div class="news-item">
          <div class="news-thumb" role="img" aria-label="News photo"></div>
          <div>
            <h4>New archive records now online</h4>
            <p>Parish registers from three counties added to our search service.</p>
          </div>
        </div>
        <div class="news-item">
          <div class="news-thumb" role="img" aria-label="News photo"></div>
          <div>
            <h4>Free talk on tracing heirs</h4>
            <p>Join us next month for an evening on probate research methods.</p>
          </div>
        </div>
      </aside>
    </div>
  </main>

  <footer class="site-footer">
    <div class="foot-col foot-map">
      <h4>Map</h4>
      <div class="map-area" role="img" aria-label="Street map showing the office location"></div>
    </div>
    <div class="foot-col foot-contact">
      <h4>Contact</h4>
      <div class="contact-line">
        <svg width="10" height="13" viewBox="0 0 10 13"><path d="M5 0a5 5 0 0 0-5 5c0 3.5 5 8 5 8s5-4.5 5-8a5 5 0 0 0-5-5z" fill="#aaa"/><circle cx="5" cy="5" r="1.8" fill="#3b3c3d"/></svg>
        <span>Lineage Research Services<br>Dana Whitfield (Professional Genealogist)<br>PO Box 4120<br>Riverton, TX 75000</span>
      </div>
      <div class="contact-line">
        <svg width="11" height="11" viewBox="0 0 11 11"><path d="M2 0l2 2.5-1.2 1.5a7 7 0 0 0 4.2 4.2L8.5 7 11 9l-1.5 2C4.5 11 0 6.5 0 1.5z" fill="#aaa"/></svg>
        <span>512 - 555 - 0147</span>
      </div>
      <div class="contact-line">
        <svg width="12" height="9" viewBox="0 0 12 9"><rect width="12" height="9" rx="1" fill="#aaa"/><path d="M0.5 0.8L6 5l5.5-4.2" stroke="#3b3c3d" fill="none"/></svg>
        <span>dana@lineageresearch.example</span>
      </div>
    </div>
    <div class="foot-col foot-follow">
      <h4>Follow us</h4>
      <p>Follow our news and events through social networks</p>
      <div class="social"><span></span><span></span><span></span><span></span></div>
    </div>
  </footer>
  <div class="bottom-bar">© Copyright 2013. All Rights Reserved.</div>
</div>
</body>
</html>
```